Commercial photographer, UAV drone photography & 360 walk-through visuals

I need a business card design that is minimalist but yet pretentiously creative. My target market are architects, designers, advertising agents and marketing managers. It is important to stress that though I am asking for a minimalist design it needs to have creative impact.

Target Market(s)

Architects, interiors designers, web-designers, artists

Contact Information for Business Card

Include my name, mobile [cell] number, email, web page and the company logo. Do not to include a postal address.

Colors

Designer to choose colors to be used in the design.

Requirements
Must have
• The following information is to be included:
• Miles Perrow
• Photographer
• m: 07812 593174
• e: miles@mpframeworks.co.uk
• w: mpframeworks.co.uk

```html
<!DOCTYPE html>
<html lang="en">
<head>
<meta charset="utf-8">
<title>MP Frameworks – Business Card</title>
<link href="https://fonts.googleapis.com/css2?family=Jost:wght@400&family=Roboto:wght@400&display=swap" rel="stylesheet">
<style>
  :root {
    --backdrop: #1c1c1c;
    --card: #0b0b0b;
    --card-edge: #1a1a1a;
    --ink: #ffffff;
    --silver: #b9b9b9;
    --rule: #d8d8d8;
  }
  * { margin: 0; padding: 0; box-sizing: border-box; }
  html, body {
    width: 1200px; height: 1200px; overflow: hidden;
    background: var(--backdrop);
  }
  .canvas {
    position: relative; width: 1200px; height: 1200px;
    display: flex; flex-direction: column; align-items: center; justify-content: center; gap: 56px;
  }
  .card {
    position: relative; width: 840px; height: 480px;
    background: var(--card);
    border: 1px solid var(--card-edge);
    border-radius: 26px;
    box-shadow: 0 18px 40px rgba(0,0,0,.55);
  }
  .brand {
    display: flex; align-items: center; gap: 18px;
    font-family: "Jost", sans-serif; font-weight: 400;
    letter-spacing: .12em; text-transform: uppercase;
  }
  .brand-dot { width: 22px; height: 22px; border-radius: 50%; background: currentColor; }
  .card-front .brand {
    position: absolute; left: 50%; top: 50%; transform: translate(-50%, -50%);
    color: var(--silver); font-size: 54px; white-space: nowrap;
  }
  .card-back .brand {
    position: absolute; right: 70px; top: 92px;
    color: var(--ink); font-size: 48px; white-space: nowrap;
  }
  .holder {
    position: absolute; left: 150px; top: 238px;
    font-family: "Jost", sans-serif; color: var(--ink); text-transform: uppercase; letter-spacing: .04em;
  }
  .holder-name { font-size: 25px; }
  .holder-role { font-size: 19px; margin-top: 2px; }
  .rule {
    position: absolute; left: 370px; right: 110px; top: 318px;
    height: 1px; background: var(--rule);
  }
  .contacts {
    position: absolute; right: 70px; top: 342px;
    list-style: none; font-family: "Roboto", sans-serif; color: var(--ink); font-size: 20px;
  }
  .contact { display: flex; justify-content: flex-end; align-items: center; gap: 14px; height: 34px; }
  .contact svg { width: 26px; height: 26px; flex: none; }
</style>
</head>
<body>
<main class="canvas">
  <section class="card card-front" aria-label="Card front">
    <div class="brand"><span class="brand-dot"></span>MP Frameworks</div>
  </section>

  <section class="card card-back" aria-label="Card back">
    <div class="brand"><span class="brand-dot"></span>MP Frameworks</div>
    <div class="holder">
      <p class="holder-name">Miles Perrow</p>
      <p class="holder-role">Photographer</p>
    </div>
    <div class="rule"></div>
    <ul class="contacts">
      <li class="contact">07812 593174
        <svg viewBox="0 0 26 26" aria-hidden="true"><circle cx="13" cy="13" r="13" fill="#fff"/><path d="M9 7.5l2.3-.3 1.2 3-1.4 1.1a7 7 0 0 0 3.6 3.6l1.1-1.4 3 1.2-.3 2.3c-5.2.6-10.1-4.3-9.5-9.5z" fill="#0b0b0b"/></svg>
      </li>
      <li class="contact">miles@mpframeworks.co.uk
        <svg viewBox="0 0 26 26" aria-hidden="true"><circle cx="13" cy="13" r="13" fill="#fff"/><rect x="7" y="8.5" width="12" height="9" rx="1" fill="#0b0b0b"/><path d="M7.5 9.2l5.5 4.3 5.5-4.3" fill="none" stroke="#fff" stroke-width="1.2"/></svg>
      </li>
      <li class="contact">mpframeworks.co.uk
        <svg viewBox="0 0 26 26" aria-hidden="true"><circle cx="13" cy="13" r="13" fill="#fff"/><g fill="none" stroke="#0b0b0b" stroke-width="1.4"><circle cx="13" cy="13" r="6"/><ellipse cx="13" cy="13" rx="2.6" ry="6"/><path d="M7 13h12"/></g></svg>
      </li>
    </ul>
  </section>
</main>
</body>
</html>
```